www.norvatepastimes.com

Updating website so looks futristic but yet business like and easy to navigate, essentially a good landing page with a cool picture summing up what we do, and links to the following pages, all other pages on site to be updated, Exclusive Distributor of Brimla Flex Unique Fitness Equipment Products in UK & Ireland, www.ferncrestdash.co.uk Exclusive Partners & Distributors Of Ferncrest Dash - Obstacle Races - Obstacle Hire - Obstacle Training - Adventure Events, www.jogvelmora.co.uk Adventures That Inspire. We also Health Club / Facillity Consultancy

```html
<!DOCTYPE html>
<html lang="en">
<head>
<meta charset="utf-8">
<title>Norvate Pastimes – Fitness and Leisure Specialists</title>
<link rel="stylesheet" href="https://fonts.googleapis.com/css2?family=Montserrat:wght@600;700;800;900&family=Open+Sans:wght@400;600;700&display=swap">
<style>
:root{
  --cyan:#00f0f4;
  --cyan-deep:#00c8d2;
  --ink:#0a0a0a;
  --night:#050607;
  --white:#ffffff;
  --grey:#6d7377;
  --grey-light:#eef2f3;
  --text:#2b2f31;
}
*{box-sizing:border-box;margin:0;padding:0}
html,body{width:1200px;height:2340px;overflow:hidden;background:var(--white)}
body{font-family:"Open Sans",Arial,sans-serif;color:var(--text)}
.page{width:1200px;height:2340px;display:flex;flex-direction:column}
.heading{font-family:"Montserrat",Arial,sans-serif;font-weight:800;letter-spacing:2px;text-transform:uppercase}
.btn{display:inline-flex;align-items:center;gap:12px;font-family:"Montserrat",Arial,sans-serif;font-weight:700;font-size:13px;letter-spacing:1.5px;text-transform:uppercase;padding:11px 26px;border:2px solid var(--cyan);color:var(--ink);background:var(--white)}
.btn svg{width:16px;height:10px}
.btn--solid{background:var(--cyan);box-shadow:0 0 18px rgba(0,240,244,.55)}

/* hero */
.hero{position:relative;height:455px;background:var(--night);overflow:hidden}
.hero__photo{position:absolute;inset:0;background:
  radial-gradient(ellipse at 50% 45%,rgba(150,120,110,.55),transparent 60%),
  linear-gradient(135deg,#2c3136 0%,#4a4440 40%,#23282c 70%,#101316 100%)}
.hero__shade{position:absolute;inset:0;background:linear-gradient(180deg,rgba(0,0,0,.55) 0%,rgba(0,0,0,.15) 40%,rgba(0,0,0,.6) 100%)}
.nav{position:relative;display:flex;align-items:center;justify-content:space-between;padding:26px 60px}
.brand{font-family:"Montserrat",Arial,sans-serif;font-weight:800;font-size:18px;letter-spacing:6px;color:var(--cyan);text-transform:uppercase}
.nav__links{display:flex;align-items:center;gap:30px;list-style:none}
.nav__links a{font-family:"Montserrat",Arial,sans-serif;font-weight:600;font-size:12px;letter-spacing:1.5px;color:var(--white);text-decoration:none}
.nav__cta{background:var(--cyan);color:var(--ink)!important;padding:8px 16px}
.hero__body{position:relative;text-align:center;padding-top:48px}
.hero__title{font-family:"Montserrat",Arial,sans-serif;font-weight:900;font-size:108px;line-height:1;letter-spacing:14px;color:var(--cyan);text-transform:uppercase;text-shadow:0 0 24px rgba(0,240,244,.6)}
.hero__sub{margin-top:16px;font-family:"Montserrat",Arial,sans-serif;font-weight:600;font-size:22px;letter-spacing:3px;color:var(--cyan)}
.hero__body .btn{margin-top:34px}

/* about */
.about{height:370px;display:flex;align-items:center;gap:70px;padding:0 90px 0 110px;background:var(--white)}
.about__text{flex:1}
.about__title{font-size:30px;color:var(--ink)}
.about__lead{margin-top:18px;font-family:"Montserrat",Arial,sans-serif;font-weight:700;font-size:17px;line-height:1.45;color:var(--cyan-deep)}
.about__copy{margin-top:16px;font-size:13px;line-height:1.75;color:var(--grey)}
.about__text .btn{margin-top:24px}
.collage{position:relative;width:470px;height:260px}
.collage__img{position:absolute;box-shadow:0 10px 26px rgba(0,0,0,.22)}
.collage__img--a{left:0;top:20px;width:250px;height:170px;background:linear-gradient(135deg,#3a4e66,#8aa0b4 55%,#d6dde3)}
.collage__img--b{left:190px;top:0;width:270px;height:150px;background:linear-gradient(135deg,#c9d3da,#6f8597 50%,#2d3a46)}
.collage__img--c{left:140px;top:120px;width:230px;height:140px;background:linear-gradient(135deg,#1f2a33,#55697a 55%,#b7c3cc)}

/* classes */
.classes{height:415px;background:var(--cyan);text-align:center;padding-top:56px}
.classes__title{font-size:24px;color:var(--ink)}
.cards{display:flex;justify-content:center;gap:42px;margin-top:40px}
.card{width:245px;height:245px;background:var(--white);box-shadow:0 14px 30px rgba(0,0,0,.22);text-align:center}
.card--dark{background:var(--ink)}
.card__img{height:100px}
.card__img--health{background:linear-gradient(135deg,#5a4038,#b08a72 50%,#e0c7b2)}
.card__img--wellness{background:linear-gradient(135deg,#e05a8a,#f4a35c 50%,#7ec8e8)}
.card__img--fitness{background:linear-gradient(135deg,#f2c230,#e56b3b 45%,#3fa8e0)}
.card__name{margin-top:14px;font-family:"Montserrat",Arial,sans-serif;font-weight:800;font-size:20px;letter-spacing:2px;color:var(--cyan-deep)}
.card--dark .card__name{color:var(--cyan)}
.card__copy{margin:8px 22px 0;font-size:11px;line-height:1.55;color:var(--grey)}
.card--dark .card__copy{color:#cfd6d8}
.card .btn{margin-top:12px;padding:7px 16px;font-size:10px}

/* testimonials */
.testimonials{height:540px;background:var(--white);text-align:center;padding-top:60px;position:relative;overflow:hidden}
.testimonials__title{font-size:24px;color:var(--ink)}
.carousel{position:relative;height:330px;margin-top:50px}
.quote{position:absolute;top:40px;width:420px;height:270px;background:var(--white);padding:70px 36px 0;box-shadow:0 16px 34px rgba(0,0,0,.16)}
.quote--center{left:390px;z-index:2}
.quote--left{left:-190px;opacity:.45}
.quote--right{left:970px;opacity:.45}
.avatar{position:absolute;left:50%;top:-48px;width:96px;height:96px;margin-left:-48px;border-radius:50%;border:4px solid var(--white);box-shadow:0 0 0 3px var(--cyan)}
.avatar--one{background:linear-gradient(135deg,#3b2a24,#8a6a58)}
.avatar--two{background:linear-gradient(135deg,#6a7784,#c0c9d0)}
.avatar--three{background:linear-gradient(135deg,#5b4a3e,#b89a82)}
.quote__name{font-family:"Montserrat",Arial,sans-serif;font-weight:800;font-size:16px;letter-spacing:1.5px;color:var(--cyan-deep);text-transform:uppercase}
.quote__role{margin-top:4px;font-family:"Montserrat",Arial,sans-serif;font-weight:700;font-size:11px;color:var(--ink)}
.stars{display:flex;justify-content:center;gap:4px;margin-top:8px}
.stars svg{width:14px;height:14px;fill:var(--cyan-deep)}
.quote__copy{margin-top:12px;font-size:12px;line-height:1.7;color:var(--grey)}
.dots{display:flex;justify-content:center;gap:10px;margin-top:4px}
.dots span{width:10px;height:10px;border-radius:50%;background:#cfd6d8}
.dots .is-active{background:var(--cyan-deep)}

/* contact */
.contact{height:510px;background:var(--night);text-align:center;padding-top:54px}
.contact__title{font-size:24px;color:var(--cyan)}
.contact__intro{margin:16px auto 0;width:520px;font-size:13px;line-height:1.7;color:#cfd6d8}
.form{width:540px;margin:30px auto 0;display:grid;grid-template-columns:1fr 1fr;gap:12px}
.field{height:38px;background:var(--cyan);color:#046068;font-size:12px;text-align:left;padding:11px 14px}
.field--wide{grid-column:1/3}
.field--message{grid-column:1/3;height:120px}
.form .btn{grid-column:1/3;justify-self:center;margin-top:10px;background:var(--cyan);border-color:var(--cyan)}

/* footer */
.footer{height:50px;background:var(--night);display:flex;flex-direction:column;align-items:center;justify-content:center;gap:6px;border-top:1px solid #1b1f21}
.social{display:flex;gap:14px}
.social span{width:12px;height:12px;border-radius:50%;background:var(--cyan)}
.footer__legal{font-size:10px;color:#7c8588}
</style>
</head>
<body>
<div class="page">

  <header class="hero">
    <div class="hero__photo" role="img" aria-label="Group fitness class training together in a studio"></div>
    <div class="hero__shade"></div>
    <nav class="nav">
      <span class="brand">Norvate Pastimes</span>
      <ul class="nav__links">
        <li><a href="#">HOME</a></li>
        <li><a href="#">ABOUT</a></li>
        <li><a href="#">CLASSES</a></li>
        <li><a href="#">PRODUCTS</a></li>
        <li><a href="#">EVENTS</a></li>
        <li><a class="nav__cta" href="#">CONTACT</a></li>
      </ul>
    </nav>
    <div class="hero__body">
      <h1 class="hero__title">Norvate<br>Pastimes</h1>
      <p class="hero__sub">Fitness and Leisure Specialists</p>
      <a class="btn btn--solid" href="#">Learn More
        <svg viewBox="0 0 16 10"><path d="M0 5h14M10 1l4 4-4 4" stroke="#0a0a0a" stroke-width="2" fill="none"/></svg></a>
    </div>
  </header>

  <section class="about">
    <div class="about__text">
      <h2 class="heading about__title">About Us</h2>
      <p class="about__lead">Leading consultants in the Health, Fitness and Leisure industry for over 20 years</p>
      <p class="about__copy">We are a fitness and leisure consultancy helping clubs, gyms and facilities grow. From equipment supply to full club design, our team brings decades of practical experience to every project we take on across the UK and Ireland.</p>
      <a class="btn" href="#">Read More
        <svg viewBox="0 0 16 10"><path d="M0 5h14M10 1l4 4-4 4" stroke="#00c8d2" stroke-width="2" fill="none"/></svg></a>
    </div>
    <div class="collage">
      <div class="collage__img collage__img--a" role="img" aria-label="Gym floor with training equipment"></div>
      <div class="collage__img collage__img--b" role="img" aria-label="Indoor cycling class"></div>
      <div class="collage__img collage__img--c" role="img" aria-label="Free weights rack in a fitness club"></div>
    </div>
  </section>

  <section class="classes">
    <h2 class="heading classes__title">Our Classes</h2>
    <div class="cards">
      <article class="card card--dark">
        <div class="card__img card__img--health" role="img" aria-label="Health class session"></div>
        <h3 class="card__name">HEALTH</h3>
        <p class="card__copy">Club consultancy and facility planning for healthier communities.</p>
        <a class="btn" href="#">Learn More</a>
      </article>
      <article class="card">
        <div class="card__img card__img--wellness" role="img" aria-label="Wellness group workout"></div>
        <h3 class="card__name">WELLNESS</h3>
        <p class="card__copy">Adventure events and outdoor programmes that inspire every member.</p>
        <a class="btn" href="#">Learn More</a>
      </article>
      <article class="card">
        <div class="card__img card__img--fitness" role="img" aria-label="Fitness class with colourful equipment"></div>
        <h3 class="card__name">FITNESS</h3>
        <p class="card__copy">Unique training equipment and obstacle hire for every level.</p>
        <a class="btn" href="#">Learn More</a>
      </article>
    </div>
  </section>

  <section class="testimonials">
    <h2 class="heading testimonials__title">Testimonials</h2>
    <div class="carousel">
      <blockquote class="quote quote--left">
        <div class="avatar avatar--two" role="img" aria-label="Client portrait"></div>
        <p class="quote__name">Mark Ellison</p>
        <p class="quote__role">Gym Owner, Leeds</p>
        <p class="quote__copy">Great equipment and even better support from start to finish.</p>
      </blockquote>
      <blockquote class="quote quote--center">
        <div class="avatar avatar--one" role="img" aria-label="Client portrait"></div>
        <p class="quote__name">Lena Hartwell</p>
        <p class="quote__role">Senior Healthcare Fitness Health Nurse</p>
        <div class="stars">
          <svg viewBox="0 0 24 24"><polygon points="12,2 15,9 22,9 16.5,13.5 18.5,21 12,16.8 5.5,21 7.5,13.5 2,9 9,9"/></svg>
          <svg viewBox="0 0 24 24"><polygon points="12,2 15,9 22,9 16.5,13.5 18.5,21 12,16.8 5.5,21 7.5,13.5 2,9 9,9"/></svg>
          <svg viewBox="0 0 24 24"><polygon points="12,2 15,9 22,9 16.5,13.5 18.5,21 12,16.8 5.5,21 7.5,13.5 2,9 9,9"/></svg>
          <svg viewBox="0 0 24 24"><polygon points="12,2 15,9 22,9 16.5,13.5 18.5,21 12,16.8 5.5,21 7.5,13.5 2,9 9,9"/></svg>
          <svg viewBox="0 0 24 24"><polygon points="12,2 15,9 22,9 16.5,13.5 18.5,21 12,16.8 5.5,21 7.5,13.5 2,9 9,9"/></svg>
        </div>
        <p class="quote__copy">Working with the team transformed our club. Their advice was clear, practical and delivered on time, and our members noticed the difference straight away. Highly recommended to any facility.</p>
      </blockquote>
      <blockquote class="quote quote--right">
        <div class="avatar avatar--three" role="img" aria-label="Client portrait"></div>
        <p class="quote__name">Ruth Calder</p>
        <p class="quote__role">Club Manager, Cork</p>
        <p class="quote__copy">A professional team that truly understands the leisure industry.</p>
      </blockquote>
    </div>
    <div class="dots"><span></span><span></span><span class="is-active"></span><span></span><span></span></div>
  </section>

  <section class="contact">
    <h2 class="heading contact__title">Testimonials</h2>
    <p class="contact__intro">Get in touch with our team today. We will reply within one working day to discuss your project.</p>
    <form class="form">
      <div class="field">Name</div>
      <div class="field">Email</div>
      <div class="field field--wide">Subject</div>
      <div class="field field--message">Message</div>
      <a class="btn" href="#">Send Message
        <svg viewBox="0 0 16 10"><path d="M0 5h14M10 1l4 4-4 4" stroke="#0a0a0a" stroke-width="2" fill="none"/></svg></a>
    </form>
  </section>

  <footer class="footer">
    <div class="social"><span></span><span></span><span></span><span></span><span></span><span></span></div>
    <p class="footer__legal">© 2024 Norvate Pastimes. All rights reserved.</p>
  </footer>

</div>
</body>
</html>
```